My company is all about art and painting people's walls, cars and everything you can imagine, I would like a sharp professional buisness card which still has a good creative element

Industry/Entity Type

Painting

Contact Information for Business Card

Ve Rubel Art
Canvass,Murals,Vehicles,Cover art and tattoo design
Commissions available..
Www.brightwall.example/tavmiu

```html
<!DOCTYPE html>
<html lang="en">
<head>
<meta charset="utf-8">
<title>Ve Rubel Art — Business Card</title>
<link rel="stylesheet" href="https://fonts.googleapis.com/css2?family=Merriweather:wght@900&display=swap">
<style>
  :root {
    --card-black: #000000;
    --ink-white: #ffffff;
    --outline-red: #c8141b;
    --paint-red: #d9492a;
    --paint-pink: #e98a86;
    --paint-orange: #e2662c;
    --paint-deep: #b5201f;
    --spire-grey: #5a5566;
  }
  * { margin: 0; padding: 0; box-sizing: border-box; }
  html, body {
    width: 1200px;
    height: 693px;
    overflow: hidden;
    background: var(--card-black);
  }
  .business-card {
    position: relative;
    width: 1200px;
    height: 693px;
    background: var(--card-black);
    display: flex;
  }
  .artwork-panel {
    width: 475px;
    height: 693px;
    flex: none;
    background:
      linear-gradient(90deg, transparent 0%, transparent 62%, var(--spire-grey) 88%, #3e3a48 100%),
      linear-gradient(90deg, var(--paint-orange) 0%, var(--paint-pink) 18%, var(--paint-red) 32%, var(--paint-pink) 46%, var(--paint-deep) 58%, var(--paint-orange) 70%);
  }
  .card-text {
    flex: 1;
    display: flex;
    flex-direction: column;
    align-items: center;
    font-family: "Merriweather", Georgia, serif;
    font-weight: 900;
    color: var(--ink-white);
    text-align: center;
    -webkit-text-stroke: 2px var(--outline-red);
    paint-order: stroke fill;
    text-shadow: 0 0 2px var(--outline-red);
  }
  .brand-name {
    font-size: 86px;
    line-height: 1;
    margin-top: 38px;
    letter-spacing: 0.5px;
    white-space: nowrap;
  }
  .services {
    font-size: 42px;
    line-height: 1.26;
    margin-top: 60px;
  }
  .availability {
    font-size: 42px;
    line-height: 1;
    margin-top: 50px;
  }
  .web-address {
    font-size: 34px;
    line-height: 1;
    margin-top: 64px;
    white-space: nowrap;
  }
</style>
</head>
<body>
  <main class="business-card">
    <div class="artwork-panel" role="img" aria-label="Abstract painting: dripping red, pink and orange paint behind dark grey gothic spires with thorny shapes"></div>
    <section class="card-text">
      <h1 class="brand-name">Ve Rubel Art</h1>
      <p class="services">Canvasses, Murals,<br>Vehicles, Cover Art, &amp;<br>Tattoo Design</p>
      <p class="availability">Commissions Available</p>
      <p class="web-address">www.brightwall.example/tavmiu</p>
    </section>
  </main>
</body>
</html>
```